Australia's newest tech recruitment startup

We are a new tech startup in the recruitment space.

We leverage the existing infrastructure of the recruitment network and bundle a value market based business model (like pixel flock) that appeals to business.

We are very individual, afraid of no one, minimalist, and defiantly NO "BS"!!

We're not cut price think Vellmar Auste rather than Korvani
Updates

Hey Everyone,

thanks so much for your designs. I have eliminated a lot of designs but if I havent to yours then your in with a shot. I would like to see the designs updated with a spot for our chirp handle, my blog address & our workgroup group address. 

For some designs I think some of the above would look ok on the back of the card so not to make the front look too messy. 

thanks   

Target Market(s)

Our target market is SME's young baby boomer and Gen X

Industry/Entity Type

Business

Requirements
Must have
• Company logo, doesn't have to be both

```html
<!DOCTYPE html>
<html lang="en">
<head>
<meta charset="utf-8">
<title>Corvelle Talent – Business Card</title>
<link rel="stylesheet" href="https://fonts.googleapis.com/css2?family=Open+Sans:wght@400;600&display=swap">
<style>
  :root {
    --backdrop: #ece6dc;
    --brand-blue: #00aee6;
    --card-white: #ffffff;
    --ink: #3a3a3a;
    --ink-soft: #4a4a4a;
  }
  * { margin: 0; padding: 0; box-sizing: border-box; }
  html, body {
    width: 1200px;
    height: 800px;
    overflow: hidden;
    background: var(--backdrop);
    font-family: "Open Sans", sans-serif;
  }
  .canvas {
    position: relative;
    width: 1200px;
    height: 800px;
  }
  .card {
    position: absolute;
    width: 294px;
    height: 480px;
  }
  .card-front {
    left: 276px;
    top: 88px;
    background: var(--brand-blue);
    border-radius: 28px 0 28px 0;
    display: flex;
    justify-content: center;
  }
  .brand-name {
    margin-top: 128px;
    color: var(--card-white);
    font-weight: 600;
    font-size: 34px;
    letter-spacing: -0.5px;
    white-space: nowrap;
  }
  .card-back {
    left: 613px;
    top: 210px;
    background: var(--card-white);
    border-radius: 0 14px 28px 0;
  }
  .holder-name {
    position: absolute;
    left: 26px;
    top: 40px;
    font-size: 20px;
    font-weight: 400;
    color: var(--ink);
    letter-spacing: 0.3px;
  }
  .holder-role {
    position: absolute;
    left: 26px;
    top: 72px;
    font-size: 14.5px;
    font-weight: 400;
    color: var(--brand-blue);
  }
  .detail-list {
    position: absolute;
    left: 26px;
    list-style: none;
  }
  .detail-list li {
    display: flex;
    align-items: center;
    height: 24.5px;
    font-size: 13.5px;
    color: var(--ink-soft);
    letter-spacing: 0.2px;
    white-space: nowrap;
  }
  .detail-list svg {
    width: 12px;
    height: 12px;
    flex: none;
  }
  .contact-list { top: 190px; }
  .contact-list svg { margin-right: 18px; }
  .social-list { top: 358px; }
  .social-list svg { margin-right: 13px; }
  .icon-stroke { fill: none; stroke: var(--brand-blue); stroke-width: 1.3; stroke-linejoin: round; stroke-linecap: round; }
  .icon-fill { fill: var(--brand-blue); }
</style>
</head>
<body>
<main class="canvas">
  <section class="card card-front" aria-label="Card front">
    <p class="brand-name">Corvelle Talent</p>
  </section>

  <section class="card card-back" aria-label="Card back">
    <h1 class="holder-name">Marlo Venning</h1>
    <p class="holder-role">Creative Director</p>

    <ul class="detail-list contact-list">
      <li>
        <svg viewBox="0 0 12 12" aria-hidden="true"><path class="icon-stroke" d="M1.5 6 L6 1.8 L10.5 6 M2.8 5 V10.5 H9.2 V5 M5 10.5 V7.8 H7 V10.5"/></svg>
        3870 Orlin Way Tessaly
      </li>
      <li>
        <svg viewBox="0 0 12 12" aria-hidden="true"><path class="icon-fill" d="M2.2 1.2 L4.2 1 L5 3.6 L3.8 4.6 C4.4 6 5.8 7.5 7.3 8.2 L8.3 7 L11 7.8 L10.8 9.8 C10.6 10.6 9.8 11 9 10.9 C5.2 10.3 1.7 6.8 1.1 3 C1 2.2 1.4 1.4 2.2 1.2 Z"/></svg>
        0198 765 432
      </li>
      <li>
        <svg viewBox="0 0 12 12" aria-hidden="true"><rect class="icon-stroke" x="1" y="2.5" width="10" height="7.5"/><path class="icon-stroke" d="M1 2.8 L6 6.8 L11 2.8"/></svg>
        hello@corvelletalent.com
      </li>
    </ul>

    <ul class="detail-list social-list">
      <li>
        <svg viewBox="0 0 12 12" aria-hidden="true"><circle class="icon-fill" cx="6" cy="6" r="4.5"/></svg>
        chirp/marlovenning
      </li>
      <li>
        <svg viewBox="0 0 12 12" aria-hidden="true"><circle class="icon-stroke" cx="6" cy="6" r="4.8"/><ellipse class="icon-stroke" cx="6" cy="6" rx="2" ry="4.8"/><path class="icon-stroke" d="M1.2 6 H10.8"/></svg>
        myblog/marlovenning
      </li>
      <li>
        <svg viewBox="0 0 12 12" aria-hidden="true"><rect class="icon-fill" x="1.5" y="1.5" width="9" height="9"/></svg>
        workgroup/marlovenning
      </li>
    </ul>
  </section>
</main>
</body>
</html>
```